Motivationsplakat
Sehr schönes Design und sehr angenehme Zusammenarbeit. Ging umgehend auf meine Wünsche ein. Immer wieder gerne! Vielen Dank!
Zielgruppe
Wir, der SC Wendorf aus der Schweiz, sind ein Fussballverein welcher in der 4. höchsten Liga spielt. Der hier zu erstellende Banner (Fusszeile) ist vorwiegend für die Spieler der 1. Mannschaft, als 'Motivationsspritze' auf diversen Plakaten (z.B. auf A1 Plakat wo die Aufstellung draufgeschrieben wird), gedacht.
Aufgabenstellung
Der Banner (als Fussleiste eines Plakates oder als eigenständiger Banner benutzbar) sollte ein Verhältniss von 1 zu 4 haben (also z.B. 50 cm hoch und 200 cm breit). Auf dem Banner muss das Logo des SC Wendorf drauf sein (im Anhang). Dazu muss es folgende Texte enthalten:
- Saison 2017/18
- Die Leidenschaft und den Verein im Herzen!
Der Spruch sollte als zentrale Botschaft verstanden werden und durch die grafische Gestalltung verstärkt/unterstützt werden.
Im Anhang sende ich ihnen noch ein paar Fotos von Spielern, welche sie eventuell verwenden könnten (muss nicht sein). Es dürften jedoch keine Spielergesichter erkennbar sein, also nur z.B. das Dress.

```html
<!DOCTYPE html>
<html lang="de">
<head>
<meta charset="utf-8">
<title>SC Wendorf – Saison 2017/18</title>
<link rel="stylesheet" href="https://fonts.googleapis.com/css2?family=Barlow:wght@600;700&display=swap">
<style>
  :root {
    --night: #000000;
    --turf-dark: #1f4a12;
    --turf: #3f8a22;
    --turf-light: #7cc04a;
    --club-red: #e30613;
    --white: #ffffff;
  }
  html, body {
    margin: 0;
    padding: 0;
    width: 1200px;
    height: 300px;
    overflow: hidden;
    background: var(--night);
  }
  .banner {
    position: relative;
    width: 1200px;
    height: 300px;
    overflow: hidden;
    font-family: "Barlow", "Arial Narrow", sans-serif;
  }
  .pitch-photo {
    position: absolute;
    inset: 0;
    background:
      radial-gradient(ellipse 520px 200px at 560px 300px, rgba(160,220,110,0.55), rgba(160,220,110,0) 70%),
      linear-gradient(to bottom, var(--night) 0%, var(--night) 42%, var(--turf-dark) 62%, var(--turf) 82%, var(--turf-light) 100%);
  }
  .headline {
    position: absolute;
    left: 0;
    top: 22px;
    width: 1172px;
    margin: 0;
    text-align: center;
    color: var(--club-red);
    font-weight: 700;
    font-size: 64px;
    line-height: 60px;
    letter-spacing: 1px;
    text-transform: uppercase;
  }
  .season {
    position: absolute;
    left: 0;
    top: 152px;
    width: 1130px;
    margin: 0;
    text-align: center;
    color: var(--white);
    font-weight: 600;
    font-size: 42px;
    line-height: 44px;
    letter-spacing: 1px;
    text-transform: uppercase;
  }
  .club-name {
    position: absolute;
    left: 896px;
    top: 162px;
    width: 264px;
    text-align: center;
    color: var(--white);
    font-weight: 700;
    font-size: 44px;
    line-height: 50px;
    letter-spacing: 1px;
    text-transform: uppercase;
  }
</style>
</head>
<body>
  <main class="banner">
    <div class="pitch-photo" role="img" aria-label="Nächtlicher Fussballrasen im Flutlicht, oben schwarz"></div>
    <h1 class="headline">Die Leidenschaft und den<br>Verein im Herzen!</h1>
    <p class="season">Saison 2017/18</p>
    <div class="club-name">SC Wendorf</div>
  </main>
</body>
</html>
```